Investment Funding, Building and Construction

I need a design logo for my new business based out of Houston, TX called Kestrel Ridge Holdings LLC., We are a company looking to help fund and invest into other small/businesses that do not want to deal with the banking system. We also remodel, renovate, and build from the ground up anything from residential, industrial warehousing, and commercial buildings. We would like the design to express our great deal of passion that we have for the work, our dedication to helping the costumer/businesses receive their expectation of work and also our professionalism and commitment to making sure we get the job done as perfect as possible. We want to build your future!

Target Market(s)

Architects, Design Companies, Home Owners and Real Estate

Industry/Entity Type

Construction Company

Contact Information for Business Card

Name: Dorian Welsby
Position: CEO/President
Company Name: Kestrel Ridge Holdings LLC.,
Website: www.kestrelridgeholds.example
Phone: 281-555-0173
Email: kestrelridgeholds@mailbox.example, crewfundline@mailbox.example

Font styles to use
Serif

Colors
f04a50
3377b5

Requirements
Must have
• Motivational, Inspiring, and Detailed oriented work but simple.
Nice to have
• I would like to see excitement and enthusiasm within the card.
Should not have
• The project can not be boring and lack of detail.

```html
<!DOCTYPE html>
<html lang="en">
<head>
<meta charset="utf-8">
<title>Kestrel Ridge Holdings LLC. – Business Card</title>
<link href="https://fonts.googleapis.com/css2?family=Noto+Serif:wght@400;600;700&display=swap" rel="stylesheet">
<style>
  :root {
    --backdrop: #8c8c8c;
    --card-light: #eeeeee;
    --navy: #023559;
    --navy-ink: #0d3a63;
    --red: #a8151b;
    --text: #3a3a3a;
    --rule: #9a9a9a;
    --white: #ffffff;
  }
  * { margin: 0; padding: 0; box-sizing: border-box; }
  html, body { width: 1200px; height: 1200px; overflow: hidden; }
  body {
    background: var(--backdrop);
    position: relative;
    font-family: "Noto Serif", Georgia, serif;
  }
  .card {
    position: absolute;
    top: 310px;
    height: 594px;
    box-shadow: 2px 3px 6px rgba(0,0,0,0.35);
  }
  .card--front { left: 234px; width: 364px; background: var(--card-light); }
  .card--back  { left: 627px; width: 370px; background: var(--navy); }

  .brand {
    position: absolute;
    left: 0; right: 0;
    text-align: center;
    font-family: "Noto Serif", Georgia, serif;
    font-weight: 700;
    letter-spacing: 0.5px;
    line-height: 1.2;
  }
  .brand__square {
    display: block;
    width: 18px; height: 18px;
    margin: 0 auto 14px;
  }
  .card--front .brand { top: 128px; color: var(--navy-ink); font-size: 26px; }
  .card--front .brand__square { background: var(--navy-ink); }
  .card--back .brand { top: 254px; color: var(--white); font-size: 27px; }
  .card--back .brand__square { background: var(--white); }

  .person {
    position: absolute;
    top: 340px; left: 0; right: 0;
    text-align: center;
  }
  .person__name {
    font-weight: 600;
    font-size: 21px;
    letter-spacing: 0.3px;
    color: var(--red);
    line-height: 1.25;
  }
  .person__title { font-size: 16px; color: var(--text); line-height: 1.35; }

  .rule {
    position: absolute;
    left: 78px; width: 208px;
    height: 1px;
    background: var(--rule);
  }
  .rule--top { top: 397px; }
  .rule--bottom { top: 507px; }

  .contact {
    position: absolute;
    top: 408px; left: 0; right: 0;
    text-align: center;
    font-size: 15px;
    line-height: 21.5px;
    color: var(--text);
    list-style: none;
  }
  .contact__label { color: var(--red); font-weight: 600; }
  .web { font-weight: 600; font-size: 15px; }
  .web__accent { color: var(--red); }
  .web__name { color: var(--navy-ink); }

  .address {
    position: absolute;
    top: 514px; left: 0; right: 0;
    text-align: center;
    font-size: 15.5px;
    line-height: 21.5px;
    color: var(--text);
    font-style: normal;
  }
  .card--back .site {
    position: absolute;
    top: 517px; left: 0; right: 0;
    text-align: center;
    color: var(--white);
    font-weight: 600;
    font-size: 15.5px;
  }
</style>
</head>
<body>
  <section class="card card--front">
    <div class="brand">
      <span class="brand__square"></span>
      KESTREL RIDGE<br>HOLDINGS LLC.
    </div>
    <div class="person">
      <p class="person__name">DORIAN WELSBY</p>
      <p class="person__title">CEO/President</p>
    </div>
    <div class="rule rule--top"></div>
    <ul class="contact">
      <li><span class="contact__label">P:</span> 281-555-0173</li>
      <li><span class="contact__label">M:</span> 281-555-0173</li>
      <li><span class="contact__label">E:</span> kestrelridgeholds@mailbox.example</li>
      <li class="web"><span class="web__accent">www.</span><span class="web__name">kestrelridgeholds</span><span class="web__accent">.example</span></li>
    </ul>
    <div class="rule rule--bottom"></div>
    <address class="address">4810 Alder Bend Road,<br>Houston, TX 77002.</address>
  </section>

  <section class="card card--back">
    <div class="brand">
      <span class="brand__square"></span>
      KESTREL RIDGE<br>HOLDINGS LLC.
    </div>
    <p class="site">www.kestrelridgeholds.example</p>
  </section>
</body>
</html>
```